Website - Tides Of Bloom

We are catalysts of change in people's lives.
We work with individuals and professionals to bring about instant substantial & transforming change in their lives.
We provide one-on-one lifestyle coaching by an experienced practitioner.
Our existing website is www.tidesofbloom.biz & this site contains our the basis for the content of our desired new project, so please examine this carefully.
We require a professional and captivating website that will instantly impress, engage invite our readers to click & invest their lives.
Our services do not come cheap, but are second to none.
Our website must be contemporary whilst reflecting indisputable class & ultra-confidence in the success of our work.
Target Market(s)
Those who seek to want to change in their lives. Those aged primarily between 30 and 50 years of age, male or female.
Industry/Entity Type
Work
Look and feel

```html
<!DOCTYPE html>
<html lang="en">
<head>
<meta charset="utf-8">
<title>Tides Of Bloom — Individual</title>
<link href="https://fonts.googleapis.com/css2?family=Sacramento&family=Roboto:wght@300;400&display=swap" rel="stylesheet">
<style>
  :root {
    --nav-teal: #5bb8cc;
    --nav-text: #ffffff;
    --nav-active: #e9f6f9;
    --ink: #4b4b4b;
    --body-ink: #555555;
    --glow-pale: #eef0c8;
    --glow-green: #c9d199;
    --olive: #a9ad72;
    --autumn: #d8924e;
    --autumn-deep: #b9652f;
  }
  * { margin: 0; padding: 0; box-sizing: border-box; }
  html, body { width: 1200px; height: 554px; overflow: hidden; }
  body { position: relative; font-family: "Roboto", sans-serif; background: var(--glow-green); }

  .site-nav {
    position: absolute; top: 0; left: 0; width: 1200px; height: 30px;
    background: var(--nav-teal); z-index: 2;
    display: flex; align-items: center; justify-content: center;
  }
  .site-nav ul { list-style: none; display: flex; align-items: center; }
  .site-nav li {
    color: var(--nav-text); font-size: 10px; font-weight: 400;
    letter-spacing: 0.6px; text-transform: uppercase;
  }
  .site-nav li + li::before { content: "•"; margin: 0 7px; font-size: 8px; }
  .site-nav li.is-active { color: var(--nav-active); font-weight: 300; }

  .hero-photo {
    position: absolute; top: 30px; left: 0; width: 1200px; height: 524px;
    background:
      radial-gradient(ellipse 300px 260px at 820px 330px, rgba(58,47,44,0.35), rgba(58,47,44,0) 70%),
      radial-gradient(ellipse 420px 320px at 200px 140px, var(--glow-pale), rgba(238,240,200,0) 75%),
      linear-gradient(90deg, var(--glow-green) 0%, var(--olive) 20%, #d9d3a8 40%, #dcb98a 62%, var(--autumn) 82%, var(--autumn-deep) 100%);
  }

  .hero-copy { position: absolute; top: 30px; left: 0; width: 1200px; height: 524px; z-index: 1; }
  .hero-title {
    position: absolute; left: 239px; top: 44px; width: 500px;
    font-family: "Sacramento", cursive; font-weight: 400;
    color: var(--ink); font-size: 68px; line-height: 74px; text-align: center;
  }
  .hero-title span {
    display: block; white-space: nowrap;
    transform: scaleX(0.72); transform-origin: center;
  }
  .hero-text {
    position: absolute; left: 303px; top: 225px; width: 336px;
    color: var(--body-ink); font-size: 12px; font-weight: 300;
    line-height: 12px; letter-spacing: 0.35px;
  }
  .hero-text p + p { margin-top: 12px; }
</style>
</head>
<body>
  <nav class="site-nav">
    <ul>
      <li>Home</li>
      <li>Business</li>
      <li class="is-active">Individual</li>
      <li>Contact</li>
    </ul>
  </nav>

  <div class="hero-photo" role="img" aria-label="Photograph of a smiling couple embracing beside a wooden fence in autumn, soft green and orange foliage behind"></div>

  <main class="hero-copy">
    <h1 class="hero-title"><span>Individual Shift to an</span><span>Outstanding Life</span></h1>
    <div class="hero-text">
      <p>Tides Of Bloom works every day with people just like you who wish to change their lives.</p>
      <p>Mum’s &amp; Dads experiencing marriage problems or who find themselves suddenly single, teenagers who have experienced death of someone close or need to get over relationship breakdown, men with phobias, and ladies experiencing problems sleeping.&nbsp; The list is endless and we have worked with them all.</p>
      <p>The great news is that like them, you can see yourself walking out of our office free of the burden you came in with.</p>
      <p>We allow you to gain the emotional control over your life you’ve always wanted. Inappropriate emotional reactions, bursts of anger, periods of apathy, depression, sadness, anxiety, and chronic fear, prevent people from achieving the quality of life they desire.</p>
      <p>Limiting feelings like “I’m not good enough”, “I’ll never be rich” or “I don’t deserve a great marriage” stall great outcomes in your life.</p>
      <p>We even enable you to eliminate issues in your past, allowing you to move forward to your goals and desires.</p>
    </div>
  </main>
</body>
</html>
```